Winter Soccer Training

Youth Soccer Academy, I want to advertise Winter Training $195.00(Includes training for one month, Uniform) after first Month $145 per month.

Target Market(s)

kids from 5 years to 18

Industry/Entity Type

Training

Colors
3176b5

Requirements
Must have
• Winter Training
• Location: Harbor Fieldhouse
• 4827 Maple Crest rd Glendale MD 20769
• Phone:(240)555-0187
• Training Schedule
• Tuesday and Thursday
• 5:30pm to 6:30pm 5 to 10 years old
• 6:30pm to 7:30pm 11 to 15 years old
• 7:30pm to 8:30pm 16 to 19 years old
• www.velantoacademy.example
Nice to have
• Soccer Field
Should not have
• Soccer Balls

```html
<!DOCTYPE html>
<html lang="en">
<head>
<meta charset="utf-8">
<title>Winter Soccer Training</title>
<link rel="stylesheet" href="https://fonts.googleapis.com/css2?family=Anton&display=swap">
<style>
  :root {
    --page: #ffffff;
    --ink: #231f20;
    --white: #ffffff;
    --grass: #6bb42f;
    --sky-blue: #79c2ee;
    --deep-blue: #0a86c8;
    --sky-top: #bfc3c0;
    --sky-mid: #e8ebe6;
    --field-light: #86ad48;
    --field-dark: #4c8624;
  }
  * { margin: 0; padding: 0; box-sizing: border-box; }
  html, body { width: 1200px; height: 894px; overflow: hidden; background: var(--page); }
  body { position: relative; font-family: "Anton", "Impact", sans-serif; color: var(--ink); }

  .panel { position: absolute; top: 0; overflow: hidden; }
  .panel--offer { left: 0; width: 584px; height: 882px; }
  .panel--schedule { left: 601px; width: 592px; height: 887px; }

  .field-photo { position: absolute; inset: 0; }
  .panel--offer .field-photo {
    background: linear-gradient(180deg, var(--sky-top) 0%, var(--sky-mid) 30%, #d9ddd6 44%, var(--field-light) 47%, var(--field-dark) 100%);
  }
  .panel--schedule .field-photo {
    height: 460px;
    background: linear-gradient(180deg, #8c9088 0%, var(--sky-mid) 15%, #d6dad3 22%, var(--field-light) 26%, var(--field-dark) 60%);
  }

  .shapes { position: absolute; inset: 0; }

  .brand { position: absolute; display: flex; flex-direction: column; align-items: center; gap: 8px; }
  .brand__dot { width: 46px; height: 46px; border-radius: 50%; background: var(--deep-blue); }
  .brand__name { font-size: 20px; line-height: 1; color: var(--deep-blue); letter-spacing: 1px; }
  .panel--offer .brand { left: 236px; top: 96px; width: 140px; }
  .panel--schedule .brand { left: 38px; top: 726px; width: 120px; }
  .panel--schedule .brand__dot { background: var(--white); }
  .panel--schedule .brand__name { color: var(--white); }

  .headline {
    position: absolute; left: 50px; top: 360px; font-size: 55px; font-weight: 400; line-height: 1.1;
    color: var(--white); letter-spacing: -0.5px; white-space: nowrap;
    text-shadow: 2px 2px 0 var(--ink), -2px 2px 0 var(--ink), 2px -2px 0 var(--ink), -2px -2px 0 var(--ink), 3px 3px 0 var(--ink), 0 3px 0 var(--ink), 3px 0 0 var(--ink);
  }

  .pricing { position: absolute; left: 0; top: 0; color: var(--white); }
  .pricing__label { position: absolute; left: 44px; top: 600px; font-size: 36px; color: var(--ink); white-space: nowrap; }
  .pricing__amount { position: absolute; left: 34px; top: 666px; font-size: 46px; white-space: nowrap; }
  .pricing__note { position: absolute; left: 34px; top: 726px; font-size: 17px; white-space: nowrap; }
  .pricing__then { position: absolute; left: 34px; top: 768px; font-size: 15px; white-space: nowrap; }
  .pricing__monthly { position: absolute; left: 42px; top: 790px; font-size: 46px; white-space: nowrap; }
  .pricing__unit { font-size: 19px; margin-left: 4px; }

  .schedule { position: absolute; left: 115px; top: 344px; }
  .schedule__title { font-size: 17px; font-weight: 400; margin-bottom: 12px; }
  .schedule__list { list-style: none; font-size: 28px; line-height: 34px; white-space: nowrap; }

  .venue { position: absolute; left: 176px; top: 702px; }
  .venue__title { font-size: 36px; font-weight: 400; line-height: 1.15; white-space: nowrap; }
  .venue__place { font-size: 14px; margin-top: 4px; }
  .venue__address, .venue__phone { font-size: 18px; line-height: 1.35; white-space: nowrap; }
  .venue__web { font-size: 17px; color: var(--white); margin-top: 8px; white-space: nowrap; }
</style>
</head>
<body>

<section class="panel panel--offer">
  <div class="field-photo" role="img" aria-label="Photo of a soccer goal on a green grass field under a cloudy sky"></div>
  <div class="brand">
    <span class="brand__dot"></span>
    <span class="brand__name">VELANTO</span>
  </div>
  <h1 class="headline">Winter Soccer Training</h1>
  <svg class="shapes" width="584" height="882" viewBox="0 0 584 882" aria-hidden="true">
    <path d="M0,578 Q260,540 584,630 L584,882 L0,882 Z" fill="var(--white)"/>
    <path d="M0,590 Q260,552 584,642 L584,882 L0,882 Z" fill="var(--grass)"/>
  </svg>
  <div class="pricing">
    <p class="pricing__label">Price:</p>
    <p class="pricing__amount">$195.00</p>
    <p class="pricing__note">( Includes 1st month and Uniform)</p>
    <p class="pricing__then">after that</p>
    <p class="pricing__monthly">$145<span class="pricing__unit">per month</span></p>
  </div>
</section>

<section class="panel panel--schedule">
  <div class="field-photo" role="img" aria-label="Photo of a soccer goal on a grass field with a player silhouette in motion"></div>
  <svg class="shapes" width="592" height="887" viewBox="0 0 592 887" aria-hidden="true">
    <path d="M0,392 C150,250 380,160 592,136 L592,887 L0,887 Z" fill="var(--white)"/>
    <path d="M0,404 C150,262 380,172 592,150 L592,887 L0,887 Z" fill="var(--sky-blue)"/>
    <path d="M0,588 Q300,548 592,664 L592,887 L0,887 Z" fill="var(--white)"/>
    <path d="M0,596 Q300,556 592,672 L592,887 L0,887 Z" fill="var(--deep-blue)"/>
  </svg>

  <div class="schedule">
    <h2 class="schedule__title">Training Schedule</h2>
    <ul class="schedule__list">
      <li>Tuesday and Thursday</li>
      <li>5:30 to 6:30 pm from 5 to 10 years old</li>
      <li>6:30 to 7:30 pm from 11 to 15 years old</li>
      <li>7:30 to 8:30 pm from 16 to 19 years old</li>
    </ul>
  </div>

  <div class="brand">
    <span class="brand__dot"></span>
    <span class="brand__name">VELANTO</span>
  </div>

  <div class="venue">
    <h2 class="venue__title">Winter Soccer Training</h2>
    <p class="venue__place">Location: Harbor Fieldhouse</p>
    <p class="venue__address">4827 Maple Crest rd Glendale MD 20769</p>
    <p class="venue__phone">Phone: (240)555-0187</p>
    <p class="venue__web">www.velantoacademy.example</p>
  </div>
</section>

</body>
</html>
```